Uprising SaaS company needs an attractive business card design

We're an uprising SaaS company who's attempting to attack the rigid car (insurance) claims management market in Europe.
We want to our mighty base order management system, listen to our clients to connect the smart ideas to build something even mightier.
We primarily focus on helping our customers manage their customers' claims/orders and get them resolved as smoothly as possible.
We'd like the business card design to express technical innovation and the fact that we connect smart ideas, as our company slogan indicates.
Contact Information for Business Card
Name, position, website, email, mobile, business address
Font styles to use
Colors
Designer to choose colors to be used in the design.
Look and feel
Each slider illustrates characteristics of the customer's brand and the style your logo design should communicate.

```html
<!DOCTYPE html>
<html lang="en">
<head>
<meta charset="utf-8">
<title>veltrano – business cards</title>
<link rel="stylesheet" href="https://fonts.googleapis.com/css2?family=Questrial&display=swap">
<style>
  :root {
    --stage: #2a7597;
    --card: #12112a;
    --card-deep: #0f0e24;
    --accent: #7fd3ec;
    --muted: #9c9ca8;
    --ink: #e6e6ee;
    --rule: #5a5a6a;
    --art: #1d1c38;
  }
  * { margin: 0; padding: 0; box-sizing: border-box; }
  html, body { width: 1200px; height: 1000px; overflow: hidden; }
  body {
    background: var(--stage);
    font-family: "Questrial", sans-serif;
    display: flex;
    flex-direction: column;
    align-items: center;
    justify-content: center;
    gap: 40px;
  }
  .card {
    position: relative;
    width: 700px;
    height: 440px;
    background: var(--card);
    border-radius: 4px;
    overflow: hidden;
    box-shadow: 0 10px 24px rgba(0,0,0,.25);
  }
  .card--back { background: var(--card-deep); }
  .vehicle-art {
    position: absolute;
    border-radius: 40% 40% 12% 12%;
    background: radial-gradient(ellipse at 50% 40%, #24233f 0%, var(--art) 60%, rgba(29,28,56,0) 100%);
  }
  .card--front .vehicle-art { left: 250px; top: 60px; width: 330px; height: 300px; }
  .card--back .vehicle-art { left: 140px; top: 170px; width: 430px; height: 270px; }
  .wordmark {
    position: absolute;
    color: var(--muted);
    letter-spacing: 1px;
    display: flex;
    align-items: center;
    gap: 12px;
  }
  .wordmark__dot {
    width: 12px; height: 12px; border-radius: 50%;
    background: var(--accent);
  }
  .card--front .wordmark { right: 48px; top: 58px; font-size: 58px; }
  .card--back .wordmark { left: 50%; top: 50%; transform: translate(-50%, -50%); font-size: 80px; }
  .divider {
    position: absolute;
    left: 48px; right: 48px; top: 152px;
    height: 1px; background: var(--rule);
  }
  .person { position: absolute; left: 48px; top: 218px; }
  .person__name { color: var(--accent); font-size: 26px; }
  .person__role { color: var(--muted); font-size: 22px; margin-top: 4px; padding-bottom: 12px; border-bottom: 1px solid var(--rule); width: 240px; }
  .contacts { position: absolute; left: 48px; top: 318px; list-style: none; }
  .contacts li { display: flex; align-items: center; gap: 12px; color: var(--ink); font-size: 19px; margin-bottom: 10px; }
  .contacts svg { width: 16px; height: 16px; fill: none; stroke: var(--accent); stroke-width: 1.6; }
  .address { position: absolute; right: 48px; top: 178px; text-align: right; color: var(--ink); font-size: 18px; line-height: 1.5; }
</style>
</head>
<body>
  <section class="card card--front">
    <div class="vehicle-art" role="img" aria-label="Faint illustration of a car seen from the front"></div>
    <div class="wordmark"><span class="wordmark__dot"></span>veltrano</div>
    <div class="divider"></div>
    <address class="address">veltrano GmbH<br>Lindenweg 14b<br>10115 Berlin - Germany</address>
    <div class="person">
      <p class="person__name">Jonas Keller</p>
      <p class="person__role">CEO</p>
    </div>
    <ul class="contacts">
      <li><svg viewBox="0 0 16 16"><path d="M3 2h3l1.5 3.5-2 1.2a8 8 0 0 0 3.8 3.8l1.2-2L14 10v3a1 1 0 0 1-1 1A11 11 0 0 1 2 3a1 1 0 0 1 1-1z"/></svg>(030) 555-0182</li>
      <li><svg viewBox="0 0 16 16"><rect x="1.5" y="3.5" width="13" height="9"/><path d="M1.5 3.5 8 9l6.5-5.5"/></svg>(030) 555-0182</li>
      <li><svg viewBox="0 0 16 16"><circle cx="8" cy="8" r="6.5"/><path d="M1.5 8h13M8 1.5c-3 3.5-3 9.5 0 13M8 1.5c3 3.5 3 9.5 0 13"/></svg>https veltrano.com</li>
    </ul>
  </section>
  <section class="card card--back">
    <div class="vehicle-art" role="img" aria-label="Faint illustration of a car seen from the front"></div>
    <div class="wordmark"><span class="wordmark__dot"></span>veltrano</div>
  </section>
</body>
</html>
```